Invitation Design Project

I need a customized graphic design for my wedding invitation.I want it to be non-traditional wedding invite. The design in mind is like a movie poster graphics while adopting 'the brighter days of the islands' font style and colors that create a light mood at the front page.Inside pages can be similar to movie posters with dark background similar to that of Ashen warden.Wedding related art/graphics can be integrated within the design.Wordings can be discussed later.

Industry/Entity Type

Graphic Design

Requirements
Must have
• Other must have features are our pictures as couple which will be sent .
Nice to have
• we would like to have the words

"our wedding.

more fun if you'll come!"

on the front cover.

```html
<!DOCTYPE html>
<html lang="en">
<head>
<meta charset="utf-8">
<title>Our Wedding – You Are Invited</title>
<link rel="stylesheet" href="https://fonts.googleapis.com/css2?family=Rubik+Dirt&family=Comfortaa:wght@700&display=swap">
<style>
  :root {
    --magenta-core: #d0167f;
    --magenta-edge: #7e0a4e;
    --splash-light: #f28a9c;
    --splash-deep: #e8455f;
    --tape-yellow: #f7e600;
    --tape-orange: #f49a1c;
    --tape-ink: #1c1414;
    --white: #ffffff;
  }
  html, body {
    margin: 0;
    padding: 0;
    overflow: hidden;
  }
  .invitation {
    position: relative;
    width: 1200px;
    height: 938px;
    overflow: hidden;
    background: radial-gradient(ellipse at 50% 45%, var(--magenta-core) 0%, #b80f71 45%, var(--magenta-edge) 100%);
  }
  .artwork {
    position: absolute;
    inset: 0;
  }
  .tape-text {
    font-family: "Comfortaa", sans-serif;
    font-weight: 700;
    font-size: 20px;
    fill: var(--tape-ink);
  }
  .headline {
    position: absolute;
    left: 782px;
    top: 300px;
    transform: rotate(-10deg);
    transform-origin: left bottom;
    color: var(--white);
    line-height: 0.9;
  }
  .headline__our,
  .headline__wedding {
    font-family: "Rubik Dirt", sans-serif;
    display: block;
  }
  .headline__our { font-size: 42px; }
  .headline__wedding { font-size: 58px; }
  .headline__tagline {
    display: block;
    margin-top: 6px;
    margin-left: 30px;
    font-family: "Comfortaa", sans-serif;
    font-weight: 700;
    font-size: 27px;
    white-space: nowrap;
  }
  .rsvp-call {
    position: absolute;
    left: 862px;
    top: 612px;
    transform: rotate(-11deg);
    transform-origin: left top;
    color: var(--white);
    font-family: "Rubik Dirt", sans-serif;
  }
  .rsvp-call__lead {
    display: block;
    font-size: 31px;
    margin-left: 0;
  }
  .rsvp-call__word {
    display: inline-block;
    margin-top: 4px;
    margin-left: 12px;
    padding: 2px 14px;
    font-size: 50px;
    border: 3px solid var(--white);
    border-radius: 6px;
    line-height: 1;
  }
</style>
</head>
<body>
<main class="invitation">
  <svg class="artwork" width="1200" height="938" viewBox="0 0 1200 938" xmlns="http://www.w3.org/2000/svg">
    <defs>
      <radialGradient id="splash-fill" cx="50%" cy="45%" r="60%">
        <stop offset="0%" stop-color="var(--splash-deep)"/>
        <stop offset="70%" stop-color="var(--splash-light)"/>
        <stop offset="100%" stop-color="var(--splash-light)" stop-opacity="0.7"/>
      </radialGradient>
      <linearGradient id="couple-fill" x1="0" y1="0" x2="0" y2="1">
        <stop offset="0%" stop-color="#e7b79c"/>
        <stop offset="35%" stop-color="#ec3f88"/>
        <stop offset="70%" stop-color="#3a3432"/>
        <stop offset="100%" stop-color="#2b2725"/>
      </linearGradient>
      <linearGradient id="drops-fill" x1="0" y1="0" x2="1" y2="1">
        <stop offset="0%" stop-color="#2c9ee0"/>
        <stop offset="55%" stop-color="#f4d20e"/>
        <stop offset="100%" stop-color="#e2187f"/>
      </linearGradient>
    </defs>

    <path class="paint-splash" role="img" aria-label="Coral and pink paint splatter behind the couple"
      fill="url(#splash-fill)"
      d="M260 300 C300 240 380 260 420 230 C470 180 560 200 600 170 C660 150 720 190 780 200 C840 220 880 300 860 380 C880 460 860 540 820 600 C790 660 700 690 620 700 C540 720 440 700 360 680 C290 660 240 600 250 540 C220 480 210 400 260 300 Z"/>

    <g class="tape tape--yellow" transform="translate(0 674) rotate(-13.4)">
      <rect x="-60" y="-16" width="1400" height="32" fill="var(--tape-yellow)"/>
      <text class="tape-text" x="-40" y="7">our Wedding ▫ our Wedding ▫ our Wedding ▫ our Wedding ▫ our Wedding ▫ our Wedding ▫ our Wedding ▫ our Wedding</text>
    </g>
    <g class="tape tape--orange" transform="translate(0 717) rotate(-13.4)">
      <rect x="-60" y="-16" width="1400" height="32" fill="var(--tape-orange)"/>
      <text class="tape-text" x="-10" y="7">our Wedding ▫ our Wedding ▫ our Wedding ▫ our Wedding ▫ our Wedding ▫ our Wedding ▫ our Wedding ▫ our Wedding</text>
    </g>

    <rect class="couple-photo" role="img" aria-label="Photo of the couple standing together, embracing and smiling"
      x="393" y="199" width="468" height="739" rx="40" fill="url(#couple-fill)"/>

    <path class="color-drops" role="img" aria-label="Blue, yellow and magenta paint drops"
      fill="url(#drops-fill)"
      d="M850 152 C885 152 900 190 895 215 C930 190 965 205 955 240 C945 280 905 300 880 340 C860 310 820 295 790 285 C770 260 800 245 820 250 C815 215 820 160 850 152 Z"/>
  </svg>

  <h1 class="headline">
    <span class="headline__our">OUR</span>
    <span class="headline__wedding">WEDDING</span>
    <span class="headline__tagline">more fun.. if you will come</span>
  </h1>

  <p class="rsvp-call">
    <span class="rsvp-call__lead">YOU ARE</span>
    <span class="rsvp-call__word">INVITED</span>
  </p>
</main>
</body>
</html>
```